Beautiful & Elegant Digital Brochure Needed For Luxury Real Estate Development

Hello,

Our company is seeking a beautiful design for our real estate development that is currently being launched.

About The Project:
Development Name - Harrow Mill Estate
Location - Charleston, S.C.
Low-Country Southern Style Architecture
Surfle "low-country" Charleston, SC to get an idea of the unique culture of the city
Surfle "copper birch tree" Charleston, SC to understand the branding

Other Digital Brochures that we love

http://www.vintrelodges.example/dunmerecove/wp-content/uploads/sites/6/2014/08/adventures-brochure.pdf

Why we like it... We love the classy feeling the brochure portrays by using unique fonts and backgrounds (burlap textures). We also love the images that represent a "low-country" vibe.

Requirements:
1. We will be providing all of the content (attached)

2. Please use plenty of southern low-country stock images from RapidLensPics (we have a subscription so just use the watermarked images unless you have full permissions)

3. Do not copy the Dunmere Cove brochure - create a unique vision that fits in to the low-country and southern vibe

4. Attached is our logos

The font we like to use is - Caslon Antique / italic
Thank you!

Target Market(s)

High net worth individuals - each homesite will be over 6 million dollars USD

Industry/Entity Type

Real Estate Development

Font styles to use
Script
Other font styles liked:
• Caslon Antique & Italic

Colors
abd036
00a990
acd036
9bcb3c
33b8a4
86cfc6
cfeae6

Requirements
Must have
• low country feeling
Nice to have
• burlap, wood backgrounds
Should not have
• Should NOT be corporate. This brochure is for multi-millionaire home buyers and investors. They are seeking simple, beautiful, quiet, serene, and southern lifestyles on the Intracoastal waterway on Wexley Cay, Charleston, South Carolina.

```html
<!DOCTYPE html>
<html lang="en">
<head>
<meta charset="utf-8">
<title>Harrow Mill Estate Brochure Spreads</title>
<link rel="stylesheet" href="https://fonts.googleapis.com/css2?family=IM+Fell+English:ital@0;1&family=Pinyon+Script&display=swap">
<style>
:root{
  --backdrop:#a3a3a3;
  --paper:#f8f6f2;
  --ink:#2a2520;
  --gold:#9a7a3e;
  --bark:#5e3e27;
  --bark-dark:#3b2515;
  --bark-light:#80583a;
  --seam:rgba(28,16,8,.55);
  --veil:rgba(200,166,112,.8);
  --cream:#fff8ea;
}
*{margin:0;padding:0;box-sizing:border-box}
html,body{width:856px;height:1200px;overflow:hidden;background:var(--backdrop)}
body{position:relative;font-family:"IM Fell English",Georgia,serif;color:var(--ink)}
.spread{position:absolute;left:70px;width:716px;height:530px;background:var(--paper);overflow:hidden;box-shadow:0 6px 18px rgba(0,0,0,.28)}
.spread--first{top:30px}
.spread--second{top:628px}
.gutter{position:absolute;left:357px;top:0;width:8px;height:100%;background:linear-gradient(90deg,rgba(0,0,0,.14),rgba(0,0,0,0));z-index:5;pointer-events:none}

.photo{position:absolute}
.photo--oak-sunburst{left:0;top:0;width:442px;height:247px;
  background:radial-gradient(ellipse 70% 85% at 60% 32%,#fff4c2 0,#e6cf78 6%,#a7a548 16%,#6f8a34 30%,#4d6a26 48%,#34481b 68%,#23301200 100%),#2a3716}
.photo--oak-sprawl{left:361px;top:247px;width:355px;height:283px;
  background:radial-gradient(ellipse 80% 70% at 50% 30%,#d6dc98 0,#a9bf5c 18%,#7d9a3c 38%,#5b6a2c 58%,#4a3c22 80%,#6a4a2c 100%)}
.photo--oak-avenue{left:275px;top:0;width:441px;height:273px;
  background:linear-gradient(180deg,#2f3d1c 0,#4a5f28 18%,#7e9444 38%,#b9c87a 52%,#9fc058 64%,#7fb03e 78%,#5c8e2a 100%)}

.wood{position:absolute;
  background:
    repeating-linear-gradient(180deg,transparent 0 13px,var(--seam) 13px 14.5px),
    repeating-linear-gradient(180deg,rgba(255,230,200,.06) 0 14.5px,rgba(0,0,0,.1) 14.5px 29px,rgba(255,220,180,.03) 29px 43.5px),
    linear-gradient(90deg,rgba(0,0,0,.18) 0,rgba(255,255,255,.04) 30%,rgba(0,0,0,.08) 60%,rgba(255,255,255,.05) 85%,rgba(0,0,0,.2) 100%),
    linear-gradient(180deg,var(--bark-light) 0,var(--bark) 45%,var(--bark-dark) 100%)}
.wood--wildlife{left:442px;top:0;width:274px;height:247px}
.wood--legends{left:0;top:0;width:275px;height:273px}

.wood-text{position:absolute;color:var(--cream);font-size:6.2px;line-height:1.56;text-align:justify}
.wood--wildlife .wood-text{left:28px;top:40px;width:222px}
.wood-text p+p{margin-top:7px}

.welcome-veil{position:absolute;left:24px;top:40px;width:113px;height:180px;background:var(--veil);padding:7px 7px;color:var(--cream);font-size:4.6px;line-height:1.56;text-align:justify}
.drop{font-family:"Pinyon Script",cursive;font-size:13px;line-height:0;color:inherit}
.heading{font-family:"IM Fell English",Georgia,serif;color:var(--gold);font-size:8.6px;font-weight:400;line-height:1.35;white-space:nowrap}
.heading .drop{font-size:17px;vertical-align:-3px;margin-right:1px}

.column{position:absolute;font-size:5.6px;line-height:1.6;text-align:justify}
.column p+p{margin-top:7px}
.column .heading{margin-bottom:12px}
.col-legend{left:24px;top:282px;width:122px}
.col-outdoor{left:172px;top:282px;width:162px}
.col-outdoor .heading{text-align:center;white-space:normal}
.photo-caption{position:absolute;left:373px;top:506px;color:var(--cream);font-size:6px;font-style:italic;opacity:.85}
.page-tab{position:absolute;left:0;bottom:0;width:110px;height:14px;background:var(--bark)}

.legends-title{position:absolute;left:0;top:112px;width:275px;text-align:center;color:var(--cream);font-size:9.6px;font-weight:400;white-space:nowrap}
.legends-title .drop{font-size:18px;vertical-align:-3px}
.legends-body{position:absolute;left:42px;top:139px;width:194px;color:var(--cream);font-size:5.7px;line-height:1.62;text-align:center}

.col-history-a{left:18px;top:290px;width:146px}
.col-history-b{left:181px;top:290px;width:162px}
.col-about{left:376px;top:286px;width:326px;font-size:5.1px}
.col-about .heading{margin-bottom:10px}
.col-about p+p{margin-top:9px}
</style>
</head>
<body>

<section class="spread spread--first">
  <div class="photo photo--oak-sunburst" role="img" aria-label="Sunlight bursting through the moss-draped limbs of an ancient copper birch tree"></div>
  <div class="welcome-veil">
    <span class="drop">N</span>estled on pristine Wexley Cay, the Harrow Mill Estate Community is a truly enviable locale. An unspoiled maritime forest and the island's meandering coastline create a stunning natural backdrop while proximity to Charleston's world-class dining and superior shops means that you never have to sacrifice comfort or style. Within the community, eighteen large private home sites offer ample space to gather in an intimate setting with family and friends while the forty acre common area provides space for large gatherings and community events. Private pools, equestrian activities, racquet sports, and golfing are among the many community-based amenities that will connect you to your neighbors. Whether you seek a peaceful escape for deep relaxation, to adopt the spirit of Southern hospitality, or to immerse yourself in the Lowcountry experience, Harrow Mill Estate is the perfect haven.
  </div>

  <div class="wood wood--wildlife">
    <div class="wood-text">
      <p><span class="drop">I</span>nland, Charleston County is home to stunning city gardens, immaculate local parks, and quaint nature trails. Terrestrial wildlife is plentiful on the island and even a short hike is likely to yield amazing photo opportunities. The island is heavily populated by South Carolina's state animal, the white tailed deer, which can be seen bounding through the wooded terrain year-round. Wild turkeys, gray fox, flying squirrels, raccoon, bobcats, and bear also call the island home. For bird watchers, a close eye on the skies will yield handsome rewards. Heron, osprey, bald eagles, red-tailed hawks, egrets, and wood storks all call the island home. Dozens of migratory species provide increased variety to an already impressive host of island regulars and are always a welcome herald to the changing seasons.</p>
      <p>Despite seeing an influx of visitors and new residents, a strong commitment to ecologically conscious growth promises that this natural wonderland will remain intact for generations to come. Coastal management, wildlife conservation, and the protection of the area's natural resources are paramount among the considerations and development is conducted responsibly and respectfully.</p>
    </div>
  </div>

  <article class="column col-legend">
    <h2 class="heading"><span class="drop">T</span>he Legend of the Copper Birch</h2>
    <p>The community is named for South Carolina's enchanting Copper Birch Tree, a centuries-old live tree located at the heart of Wexley Cay. Although the exact age of the Copper Birch is unknown, estimates based on the tree's size and condition suggest that the coastal tree is between 700 and 1500 years old. The tree predates recorded history on the island and likely stood in its ground long before the arrival of Admiral Corvane to the Americas. The ancient tree's massive, sprawling branches reach outward in all directions, covering more than 17,000 square feet of ground with its majestic shade. Standing more than 65 feet tall, the massive tree towers over the park that bears its name. This imposing beauty has become one of the area's most iconic natural wonders, drawing thousands of visitors each year. Situated amid a treasure trove of historic structures and man-made beauty, the park offers visitors a reminder of Mother Nature's strength, vitality, and splendor.</p>
  </article>

  <article class="column col-outdoor">
    <h2 class="heading"><span class="drop">E</span>mbrace Outdoor Living and Connect with Nature</h2>
    <p>Life is better when lived outdoors and in the Lowcountry, nature beckons. Wake each morning to breathtaking sunrises and allow the warm, salt-kissed air to rejuvenate your soul. Spend your days enjoying one of the area's exquisite beaches or visit some of Charleston's inspiring heritage sites. During the early evenings, enjoy dinner alfresco before retiring on the veranda with family and friends. Gather around an outdoor fireplace to share the day's memories and create even more under the stars.</p>
    <p>Featuring both community and private docks, Harrow Mill Estate is a maritime paradise. Board your vessel to explore the tidal Stono River separating Wexley Cay from the mainland or follow the Intracoastal Waterway to the sea. For the adventurous, a kayak or canoe is an ideal means for exploring the intricacies of the island's elaborate coastal marshes. Sport fishers will be pleased to find the channels teeming with flounder, cobia, mackerel, tarpon, white shrimp, and blue crabs. Non-anglers will also appreciate the plentiful array of aquatic life and availability of fresh daily seafood.</p>
  </article>

  <div class="photo photo--oak-sprawl" role="img" aria-label="Wide view of the copper birch tree's sprawling limbs across a forest clearing"></div>
  <span class="photo-caption">The legend of the Copper Birch</span>
  <div class="page-tab"></div>
  <div class="gutter"></div>
</section>

<section class="spread spread--second">
  <div class="wood wood--legends"></div>
  <h2 class="legends-title"><span class="drop">W</span>alk in the Footsteps of Legends.</h2>
  <p class="legends-body">Take a bike tour of Charleston's iconic Lantern Row, once a beacon to weary sailors; paddle along one of the area's many waterways and explore the recesses of the ancient coastline; or jog down the city's famed Battery to view the location where the first shot of the Civil War was fired. The area's rich history begs to be uncovered.</p>

  <div class="photo photo--oak-avenue" role="img" aria-label="Avenue of moss-draped live oaks arching over a green lawn"></div>

  <article class="column col-history-a">
    <p>Charleston's significance to the nation's history is nearly unrivaled. One of the earliest and most important ports along the Atlantic, Charleston was founded in 1670 and named for England's King Aldric II. Charles Towne immediately became an economic center among the southern colonies. The city grew wealthy exporting rice and cotton produced using slave labor and became a prominent force in the lucrative slave trade market. Charleston flourished economically and culturally, benefiting from routinely imported luxuries such as exotic fruits, rare spices, and fine silks. Charleston's prosperous landowners and elite aristocracy spared no expense on private and civic buildings and soon, the city grew to become the largest and most affluent south of Philadelphia. The city was home to the nation's first theater and talented artists and artisans flocked to the city where their talents were highly sought and handsomely rewarded.</p>
  </article>

  <article class="column col-history-b">
    <p>Owing to its relatively flat terrain and readily fortified barrier islands, the city quickly became a formidable military strong point along the coast. Large sea forts were erected using logs hewn from the indigenous Palmetto trees, imported granite, brick, and tabby concrete. In the 1700s, Charleston's strategic position along the eastern seaboard was essential to American forces defending Charleston Harbor and the American mainland from British invasion. A century later, when social tensions threatened to divide the country, Charleston again became an epicenter for social and political action. The city was host to the inaugural shot of the Civil War, not only marking the beginning of the days-long Battle of Fort Kestrel but also signifying the official beginning of the nation's bloodiest conflict. Today, the city is the proud home of The Bastion, one of the nation's oldest and most elite military colleges. The college's impressive list of Alumni includes some of the country's most accomplished military personnel as well as Novelists, Politicians, Astronauts, Professional Athletes, Actors, and Musicians. The college welcomes the public to many of its parades, ceremonies, and events throughout the year.</p>
  </article>

  <article class="column col-about">
    <h2 class="heading"><span class="drop">A</span>bout Wexley Cay</h2>
    <p>Set amidst a network of barrier islands on the southern border of Charleston County, South Carolina, Wexley Cay is a 50 square mile expanse of majestic coastal beauty. Originally occupied by the Stono, Kiawah, and Bohicket tribes, Wexley Cay was first settled by Europeans in the late 17th century and, as early as 1695, large farming plantations were scattered along the Stono River. Colonists also established a lucrative fur trade with the island's native tribes, shipping a surplus of deer hides to Europe during the early years. Although relations between the colonists and native inhabitants were initially amiable, a dispute over livestock brought the alliance to an end. Despite this, the Native legacy remains visible in the area today, as the island's bordering rivers (as well as many of the neighboring Sea Islands) are named after the region's first inhabitants.</p>
    <p>By the 1800s, the island was home to dozens of exquisite plantation homes and was known for producing a variety of crops including tea, rice, indigo, and tomatoes. Many of these homes remain today as beautifully preserved testaments to the island's early agricultural heritage.</p>
    <p>In 1739, Wexley Cay was home to the Stono Rebellion which claimed nearly 100 lives. The uprising began when a band of 20 enslaved Africans stole food, weapons, and ammunition from a local shopkeeper before marching southward towards the free Spanish territory of Florida. The group burned plantations and gained followers along the route, eventually swelling to more than 80 before being intercepted by local militia forces. The Stono Rebellion was one of the largest and most infamous slave revolts to have occurred throughout the colonies. Following the insurrection, Charleston's population was left fearful and anxious of future rebellions. As a result, legislation was passed prohibiting slaves from gathering in large groups, barring them from education, and preventing slave owners from granting a slave freedom. Additionally, the law temporarily halted the import of African slaves. Throughout the south, word of the Stono Rebellion traveled and inspired a number of similar uprisings.</p>
  </article>

  <div class="page-tab"></div>
  <div class="gutter"></div>
</section>

</body>
</html>
```